Webbanner-Design für Affiliate Marketing
Zielgruppe
Online-Shop für Kopfbedeckungen aller Art (Hüte, Mützen, Fascinator, Stirnbänder)
Design soll eine möglichst große Zielgruppe ansprechen (Hauptfokus: 18-34 Jahre). Also alle Online-Shopper mit einer Vorliebe für Hüte/ Mützen.
Aufgabenstellung
Insgesamt ein modernes, eingängiges und stilvolles Design. Nicht allzu verspielt oder zu unruhig. Fokus auf das Wesentliche.
Text: A Headwear for Everyone
B Hüte und Mützen, Top Auswahl, Kostenlose Lieferung
C Gut behütet durch den Winter
D Der Hut-Online-Shop
Das Lumo Vanta Logo soll mit eingebunden werden. Keine vorgegebene Platzierung, sprich dem Design anpassen.
Formate: (Breite x Höhe)
1. Full Banner - 468 x 60 Pixel, max. 40k Dateigröße
2. Medium Rectangle - 300 x 250 Pixel, max. 40k Dateigröße
3. Vertical Banner - 120 x 240 Pixel, max. 30k Dateigröße
4. Rectangle - 180 x 150 Pixel, max. 40k Dateigröße

```html
<!DOCTYPE html>
<html lang="de">
<head>
<meta charset="utf-8">
<title>Lumo Vanta – Full Banner</title>
<link rel="stylesheet" href="https://fonts.googleapis.com/css2?family=Oswald:wght@300;400;500;600&display=swap">
<style>
  :root {
    --stage: #f3f3f3;
    --panel-dark: #141414;
    --brand-red: #f2464b;
    --logo-ink: #2b2b2b;
    --white: #ffffff;
    --text-light: #f2f2f2;
    --photo-warm: #c49a84;
    --photo-dark: #2a211d;
  }
  * { box-sizing: border-box; margin: 0; padding: 0; }
  html, body {
    width: 1200px; height: 800px; overflow: hidden;
    background: var(--stage);
    font-family: "Oswald", "Arial Narrow", sans-serif;
  }
  .banner {
    position: absolute; left: 38px; top: 328px;
    width: 1123px; height: 144px;
    background: var(--panel-dark);
    overflow: hidden;
  }
  .brand-block {
    position: absolute; left: 0; top: 0; width: 338px; height: 144px;
    background: var(--white);
  }
  .brand-name {
    position: absolute; left: 0; top: 0; width: 338px; height: 89px;
    display: flex; align-items: center; justify-content: center;
    color: var(--logo-ink); font-weight: 500; font-size: 36px; letter-spacing: 2px;
    white-space: nowrap;
  }
  .brand-claim {
    position: absolute; left: 0; bottom: 0; width: 338px; height: 55px;
    background: var(--brand-red); color: var(--white);
    display: flex; align-items: center; justify-content: center;
    font-size: 29px; font-weight: 500; letter-spacing: 0.5px;
  }
  .models-photo {
    position: absolute; left: 540px; top: 0; width: 460px; height: 144px;
    background: linear-gradient(90deg, var(--panel-dark) 0%, var(--photo-dark) 15%, var(--photo-warm) 38%, var(--photo-dark) 55%, var(--photo-warm) 75%, var(--photo-dark) 90%, var(--panel-dark) 100%);
  }
  .headline {
    position: absolute; left: 355px; top: 4px;
    color: var(--white); font-size: 40px; line-height: 48px; white-space: nowrap;
  }
  .headline strong { font-weight: 600; }
  .headline span { font-weight: 300; }
  .benefits {
    position: absolute; left: 355px; top: 60px; list-style: none;
    color: var(--text-light); font-size: 21px; line-height: 26px; font-weight: 400;
  }
  .benefits li { display: flex; align-items: center; gap: 10px; }
  .benefits svg { width: 10px; height: 12px; }
  .season-line {
    position: absolute; right: 10px; top: 8px; text-align: right;
    color: var(--white); font-size: 22px; line-height: 26px; font-weight: 500;
  }
  .shop-button {
    position: absolute; left: 921px; top: 86px; width: 197px; height: 52px;
    background: var(--brand-red); color: var(--white);
    display: flex; align-items: center; justify-content: center;
    font-size: 32px; font-weight: 600; letter-spacing: 1px; text-decoration: none;
  }
</style>
</head>
<body>
  <div class="banner">
    <div class="models-photo" role="img" aria-label="Zwei junge Frauen mit Hüten, warme Haut- und dunkle Hutfarben"></div>

    <div class="brand-block">
      <div class="brand-name">LUMO VANTA</div>
      <div class="brand-claim">Der Hut-Online-Shop</div>
    </div>

    <h1 class="headline"><strong>HEADWEAR</strong> <span>for Everyone</span></h1>

    <ul class="benefits">
      <li><svg viewBox="0 0 10 12"><path d="M0 0 L10 6 L0 12 Z" fill="#ffffff"/></svg>Hüte und Mützen</li>
      <li><svg viewBox="0 0 10 12"><path d="M0 0 L10 6 L0 12 Z" fill="#ffffff"/></svg>Top Auswahl</li>
      <li><svg viewBox="0 0 10 12"><path d="M0 0 L10 6 L0 12 Z" fill="#ffffff"/></svg>Kostenlose Lieferung</li>
    </ul>

    <p class="season-line">Gut behütet<br>durch den Winter</p>

    <a class="shop-button" href="#">ZUM SHOP</a>
  </div>
</body>
</html>
```